Business Card design for new private practice opening

I need a business card design for my new private practice with my new logo uploaded as a file
On the front the logo
On the back: maybe a small logo somewhere?
Priv. Doz. DDr. Corinna Vestaluk
Fachärztin für Allgemein- & Viszeralchirurgie
Address: xxx
Tel: xxx
Mobil:xxx
Webseite:xxx
Email:xxx

Contact Information for Business Card

See project description above for details

Requirements
Nice to have
• I would like the colors of the logo incorporated into the business card

```html
<!DOCTYPE html>
<html lang="de">
<head>
<meta charset="utf-8">
<title>Vestaluk Chirurgie – Visitenkarte</title>
<link rel="stylesheet" href="https://fonts.googleapis.com/css2?family=Montserrat:wght@400;500;600&display=swap">
<style>
  :root {
    --teal: #43b3ae;
    --teal-pattern: #5cc0bb;
    --grey: #808080;
    --grey-dark: #7a7a7a;
    --white: #ffffff;
    --stage: #ececec;
  }
  * { margin: 0; padding: 0; box-sizing: border-box; }
  html, body {
    width: 1200px; height: 1199px; overflow: hidden;
    background: var(--stage);
    font-family: "Montserrat", Arial, sans-serif;
  }
  .card {
    position: absolute; left: 202px; width: 797px; height: 454px;
    overflow: hidden;
  }
  .card--front { top: 120px; background: var(--teal); }
  .card--back { top: 624px; background: var(--white); }

  .front-pattern {
    position: absolute; inset: 0;
    background: linear-gradient(135deg, var(--teal) 0%, var(--teal-pattern) 50%, var(--teal) 100%);
    opacity: .35;
  }
  .brand-mark {
    position: absolute; left: 146px; top: 154px;
    width: 148px; height: 148px; border-radius: 50%;
    border: 7px solid var(--white);
  }
  .brand-name {
    position: absolute; left: 316px; top: 170px;
    color: var(--white); font-weight: 600; font-size: 56px;
    line-height: 62px; letter-spacing: 1px; text-transform: uppercase;
  }

  .back-mark {
    position: absolute; left: 68px; top: 132px;
    width: 192px; height: 192px; border-radius: 50%;
    border: 7px solid var(--grey);
    display: flex; align-items: center; justify-content: center; text-align: center;
    color: var(--teal); font-weight: 600; font-size: 19px; line-height: 24px;
    text-transform: uppercase;
  }
  .divider {
    position: absolute; left: 319px; top: 56px;
    width: 3px; height: 342px; background: var(--teal);
  }
  .title-badge {
    position: absolute; left: 356px; top: 55px; height: 27px;
    padding: 0 12px; background: var(--teal); color: var(--white);
    font-size: 21px; font-weight: 500; line-height: 28px; letter-spacing: .5px;
  }
  .person-name {
    position: absolute; left: 356px; top: 88px;
    color: var(--grey); font-size: 34px; font-weight: 500; letter-spacing: 1px;
    text-transform: uppercase; white-space: nowrap;
  }
  .specialty {
    position: absolute; left: 356px; top: 128px;
    color: var(--teal); font-size: 19px; line-height: 28px; text-transform: uppercase;
  }
  .contact-list { position: absolute; left: 360px; top: 210px; list-style: none; }
  .contact-list li {
    display: flex; align-items: center; height: 41.5px;
    color: var(--grey-dark); font-size: 25px; letter-spacing: .5px;
  }
  .contact-list svg { width: 20px; height: 20px; margin-right: 14px; fill: var(--teal); }
</style>
</head>
<body>
  <section class="card card--front">
    <div class="front-pattern" role="img" aria-label="Dezentes Wiederholungsmuster des Praxis-Emblems auf Türkis"></div>
    <div class="brand-mark"></div>
    <div class="brand-name">Vestaluk<br>Chirurgie</div>
  </section>

  <section class="card card--back">
    <div class="back-mark">Vestaluk<br>Chirurgie</div>
    <div class="divider"></div>
    <div class="title-badge">PRIV. DOZ. DDR.</div>
    <div class="person-name">Corinna Vestaluk</div>
    <div class="specialty">Fachärztin für Allgemein-<br>Viszeralchirurgie</div>
    <ul class="contact-list">
      <li><svg viewBox="0 0 24 24"><path d="M12 2a7 7 0 0 0-7 7c0 5 7 13 7 13s7-8 7-13a7 7 0 0 0-7-7zm0 9.5A2.5 2.5 0 1 1 12 6a2.5 2.5 0 0 1 0 5.5z"/></svg>Address: xxx</li>
      <li><svg viewBox="0 0 24 24"><path d="M6.6 10.8a15 15 0 0 0 6.6 6.6l2.2-2.2a1 1 0 0 1 1-.25 11.4 11.4 0 0 0 3.6.57 1 1 0 0 1 1 1V20a1 1 0 0 1-1 1A17 17 0 0 1 3 4a1 1 0 0 1 1-1h3.5a1 1 0 0 1 1 1 11.4 11.4 0 0 0 .57 3.6 1 1 0 0 1-.25 1z"/></svg>Tel: xxx</li>
      <li><svg viewBox="0 0 24 24"><rect x="6" y="2" width="12" height="20" rx="2"/></svg>Mobil: xxx</li>
      <li><svg viewBox="0 0 24 24"><path d="M12 2a10 10 0 1 0 0 20 10 10 0 0 0 0-20zm6.9 6h-3a15 15 0 0 0-1.3-3.9A8 8 0 0 1 18.9 8zM12 4c.8 1.2 1.5 2.5 1.9 4h-3.8c.4-1.5 1.1-2.8 1.9-4zM4.3 14a8 8 0 0 1 0-4h3.4a16 16 0 0 0 0 4zm.8 2h3a15 15 0 0 0 1.3 3.9A8 8 0 0 1 5.1 16zm3-8h-3a8 8 0 0 1 4.3-3.9A15 15 0 0 0 8.1 8zM12 20c-.8-1.2-1.5-2.5-1.9-4h3.8c-.4 1.5-1.1 2.8-1.9 4zm2.3-6H9.7a14 14 0 0 1 0-4h4.6a14 14 0 0 1 0 4zm.3 5.9a15 15 0 0 0 1.3-3.9h3a8 8 0 0 1-4.3 3.9zm1.7-5.9a16 16 0 0 0 0-4h3.4a8 8 0 0 1 0 4z"/></svg>Webseite: xxx</li>
      <li><svg viewBox="0 0 24 24"><path d="M3 5h18v2l-9 6-9-6zm0 4 9 6 9-6v10H3z"/></svg>Email: xxx</li>
    </ul>
  </section>
</body>
</html>
```